Business Cards

I'd like help creating business cards with the full logo "Veltrona Capital Partners" on the back of the card (navy background with white writing), and abbreviated logo "VCP" on the front. Would like to list name, title, phone number, email, and website listed on front of card. Would like to keep very simple. Front font Arial or similar.

```html
<!DOCTYPE html>
<html lang="en">
<head>
<meta charset="utf-8">
<title>Veltrona Capital Partners — Business Cards</title>
<link rel="stylesheet" href="https://fonts.googleapis.com/css2?family=Arimo:wght@400;700&display=swap">
<style>
  :root {
    --stage: #1b1b1d;
    --navy: #173a6b;
    --navy-deep: #112e58;
    --navy-mid: #1d4378;
    --navy-light: #4f78b6;
    --white: #ffffff;
    --card-font: "Arimo", Arial, sans-serif;
  }
  * { box-sizing: border-box; margin: 0; padding: 0; }
  html, body {
    width: 1200px; height: 1059px; overflow: hidden;
    background: var(--stage);
    font-family: var(--card-font);
  }
  .canvas { position: relative; width: 1200px; height: 1059px; }

  /* Front card */
  .card-front {
    position: absolute; left: 258px; top: 89px;
    width: 689px; height: 394px;
    background: var(--navy); color: var(--white);
  }
  .card-front__frame {
    position: absolute; left: 19px; top: 20px;
    width: 650px; height: 354px;
    border: 2.5px solid var(--white);
  }
  .identity {
    position: absolute; right: 362px; top: 174px;
    text-align: right;
  }
  .identity__name {
    font-size: 21px; font-weight: 700; line-height: 24px; letter-spacing: 0.2px;
  }
  .identity__title {
    font-size: 17.5px; font-weight: 400; line-height: 22px;
  }
  .divider {
    position: absolute; left: 343px; top: 166px;
    width: 2px; height: 63px; background: var(--white);
  }
  .contact-list {
    position: absolute; left: 360px; top: 158px;
    list-style: none;
  }
  .contact-list__item {
    display: flex; align-items: center;
    height: 24.5px; font-size: 18.5px; line-height: 24px;
  }
  .contact-list__icon {
    width: 16px; height: 16px; margin-right: 10px; flex: none;
  }
  .address {
    position: absolute; left: 0; right: 0; top: 362px;
    text-align: center; font-size: 18.5px; line-height: 24px;
  }
  .address span { background: var(--navy); padding: 0 8px; }

  /* Back card */
  .card-back {
    position: absolute; left: 252px; top: 541px;
    width: 701px; height: 400px; overflow: hidden;
  }
  .card-back__pattern {
    position: absolute; inset: 0;
    background: linear-gradient(145deg, var(--navy-deep) 0%, var(--navy-mid) 45%, var(--navy-light) 100%);
  }
  .brand-name {
    position: absolute; left: 285px; top: 247px; width: 273px; height: 80px;
    display: flex; flex-direction: column; justify-content: center; align-items: center;
    color: var(--white); font-weight: 700; text-transform: uppercase;
    background: var(--navy-deep);
  }
  .brand-name__main {
    font-size: 40px; line-height: 44px; letter-spacing: 5px;
  }
  .brand-name__sub {
    font-size: 16px; line-height: 22px; letter-spacing: 5.5px;
  }
</style>
</head>
<body>
<main class="canvas">

  <section class="card-front" aria-label="Business card front">
    <div class="card-front__frame"></div>

    <div class="identity">
      <p class="identity__name">JONATHAN SMITH</p>
      <p class="identity__title">Manager</p>
    </div>

    <div class="divider"></div>

    <ul class="contact-list">
      <li class="contact-list__item">
        <svg class="contact-list__icon" viewBox="0 0 16 16" fill="none" stroke="#fff" stroke-width="1.4" stroke-linejoin="round">
          <path d="M3 1.8l2.3-.3 1.2 3-1.5 1.2a8 8 0 0 0 4.3 4.3l1.2-1.5 3 1.2-.3 2.3c-.2.8-1 1.2-1.8 1.1C6.5 12.4 3.6 9.5 2.8 4.6c-.1-.8.3-1.6 1.1-1.8z"/>
          <path d="M9.5 2.5a4.5 4.5 0 0 1 4 4M9.3 4.8a2.3 2.3 0 0 1 1.9 1.9" stroke-linecap="round"/>
        </svg>
        123-456-2100
      </li>
      <li class="contact-list__item">
        <svg class="contact-list__icon" viewBox="0 0 16 16" fill="none" stroke="#fff" stroke-width="1.4" stroke-linejoin="round">
          <rect x="1.5" y="3.5" width="13" height="9.5" rx="1"/>
          <path d="M1.8 4l6.2 5 6.2-5"/>
        </svg>
        youremail@mailbox.com
      </li>
      <li class="contact-list__item">
        <svg class="contact-list__icon" viewBox="0 0 16 16" fill="none" stroke="#fff" stroke-width="1.2">
          <circle cx="8" cy="8" r="6.5"/>
          <ellipse cx="8" cy="8" rx="2.8" ry="6.5"/>
          <path d="M1.5 8h13M2.5 4.8h11M2.5 11.2h11"/>
        </svg>
        www.yourwebsite.com
      </li>
    </ul>

    <p class="address"><span>Your Address, City, State, Zip 0000</span></p>
  </section>

  <section class="card-back" aria-label="Business card back">
    <div class="card-back__pattern" role="img" aria-label="Repeating embossed VCP monogram pattern in navy tones"></div>
    <p class="brand-name">
      <span class="brand-name__main">Veltrona</span>
      <span class="brand-name__sub">Capital Partners</span>
    </p>
  </section>

</main>
</body>
</html>
```